Silken Clouds eLiquid Label Design

We need a new label design for one of our eliquid brands. We have a logo that we like but our label is dated and we would like a fresh design that complies with upcoming KRB regulations. We are not married to a color scheme but our store colors are red, grey, black and white. Label size is 3X1.5"

Target Market(s)

young adults, adults, seniors

Font styles to use
Sans Serif
Decorative

Requirements
Must have
• KRB Compliant Labeling
Nice to have
• eye catching colors
Should not have
• bland overall design

```html
<!DOCTYPE html>
<html lang="en">
<head>
<meta charset="utf-8">
<title>Silken Clouds eLiquid Label</title>
<link href="https://fonts.googleapis.com/css2?family=Arimo:wght@400;700&family=Graduate&display=swap" rel="stylesheet">
<style>
  :root {
    --page: #ffffff;
    --label-black: #050505;
    --paper-white: #ffffff;
    --accent-blue: #1f7fcf;
    --text-white: #ffffff;
  }
  * { box-sizing: border-box; margin: 0; padding: 0; }
  html, body { width: 1200px; height: 1200px; overflow: hidden; background: var(--page); }
  .canvas { position: relative; width: 1200px; height: 1200px; background: var(--page); }
  .label {
    position: absolute; left: 60px; top: 330px; width: 1080px; height: 540px;
    background: var(--label-black);
    display: grid; grid-template-columns: 300px 480px 300px;
    font-family: "Arimo", Arial, sans-serif; color: var(--text-white);
  }
  .label::before {
    content: ""; position: absolute; left: 0; right: 0; top: 14px; height: 14px;
    background: var(--paper-white);
  }
  .panel { position: relative; text-align: center; }
  .panel-side { border-right: 2px solid #1a1a1a; }
  .panel-side:last-child { border-right: none; border-left: 2px solid #1a1a1a; }
  .side-heading { margin-top: 64px; color: var(--accent-blue); font-weight: 700; font-size: 24px; letter-spacing: 0.5px; }
  .side-body { margin: 8px auto 0; width: 240px; font-size: 23px; line-height: 1.3; }
  .side-note { position: absolute; left: 0; right: 0; top: 330px; font-size: 20px; line-height: 1.4; }
  .side-note strong { font-weight: 400; font-size: 22px; }
  .side-band {
    position: absolute; left: 0; right: 0; bottom: 28px; height: 58px;
    background: var(--paper-white); color: var(--accent-blue);
    font-size: 21px; display: flex; align-items: center; justify-content: center;
  }
  .panel-main::after {
    content: ""; position: absolute; left: 0; right: 0; bottom: 28px; height: 22px;
    background: var(--paper-white);
  }
  .brand {
    margin-top: 96px; display: flex; align-items: center; justify-content: center; gap: 16px;
    font-family: "Arimo", Arial, sans-serif; font-weight: 700; font-size: 52px; color: var(--text-white);
  }
  .brand-dot { width: 30px; height: 30px; border-radius: 50%; background: var(--accent-blue); }
  .ratio { margin-top: 66px; font-weight: 700; font-size: 30px; letter-spacing: 0.5px; }
  .flavor-badge {
    position: relative; margin: 14px auto 0; width: 300px; height: 96px;
    border: 6px solid var(--accent-blue); border-radius: 48px;
    display: flex; align-items: center; justify-content: center;
  }
  .flavor-name { font-family: "Graduate", "Arimo", serif; font-size: 56px; color: var(--text-white); line-height: 1; margin-top: -8px; }
  .strength {
    position: absolute; left: 50%; bottom: -22px; transform: translateX(-50%);
    background: var(--accent-blue); color: var(--label-black);
    border: 3px solid var(--label-black); border-radius: 20px;
    padding: 3px 18px; font-size: 22px; white-space: nowrap;
  }
  .volume { margin-top: 48px; font-size: 28px; }
</style>
</head>
<body>
<div class="canvas">
  <div class="label">
    <section class="panel panel-side">
      <h2 class="side-heading">INGREDIENTS:</h2>
      <p class="side-body">USP Kosher Vegetable Glycerin, USP Propylene Glycol, Natural and artificial Flavors. May Contain Nicotine.</p>
      <p class="side-note">Manucature for:<br><strong>Company Name</strong></p>
      <div class="side-band">Underage Sale Prohibited</div>
    </section>

    <section class="panel panel-main">
      <div class="brand"><span class="brand-name">Silken Clouds</span><span class="brand-dot"></span></div>
      <p class="ratio">70% VG - 30% PG</p>
      <div class="flavor-badge">
        <span class="flavor-name">FLAVOR</span>
        <span class="strength">0.3% Nicotine</span>
      </div>
      <p class="volume">30ml / 1 fl oz</p>
    </section>

    <section class="panel panel-side">
      <h2 class="side-heading">WARNING:</h2>
      <p class="side-body">Do Not Swallow, Avoid Eye and Skin Contact, Keep Out of Reach from Children and Pets.</p>
      <p class="side-note">Sale only allowed in the<br><strong>United States</strong></p>
      <div class="side-band">www.silkencloudsliquid.com</div>
    </section>
  </div>
</div>
</body>
</html>
```